Web Design for Palmwick Organic Soap Company

We need a website design for the company Velm Botanics based on the package design per attached.

The design should communicate high end, luxury organic. The site will provide facts about how the spread of disease causes deaths and can be prevented with hand washing. The site will also have a page about why we are passionate about organics and how that relates to our skin including skin facts.
Also, the site should have an e-commerce product page and shopping cart.

Target Market(s)

Educated, health conscious and socially conscious consumers who shop luxury. Target vendors include Tarrow Market and Bellquist..

Industry/Entity Type

E-Commerce

Font styles to use
Other font styles liked:
• See attached

Requirements
Must have
• Use of Ying Yang leaf Logo provided.
Based on design provided.

```html
<!DOCTYPE html>
<html lang="en">
<head>
<meta charset="utf-8">
<title>Velm Botanics</title>
<link href="https://fonts.googleapis.com/css2?family=Fresca&family=Noto+Sans:wght@400&family=Noto+Serif:ital,wght@0,400;0,700;1,700&display=swap" rel="stylesheet">
<style>
:root{
  --brick:#a8402a;
  --brick-soft:rgba(168,64,42,.88);
  --dark-panel:rgba(50,36,24,.82);
  --cream:#dcc39b;
  --gold:#f2d6a0;
  --body-text:#6b4a2c;
  --link-text:#6e4a28;
  --page:#ffffff;
}
*{margin:0;padding:0;box-sizing:border-box}
html,body{width:1200px;height:674px;overflow:hidden;background:var(--page)}
.page{position:relative;width:1200px;height:674px;overflow:hidden}
.masthead{position:absolute;left:109px;top:0;width:982px;height:180px;
  background:linear-gradient(110deg,#3a2c20 0%,#8c7258 30%,#5a4330 50%,#b09070 70%,#6b5038 100%)}
.brand-mark{position:absolute;left:8px;top:7px;width:109px;height:162px;background:var(--brick);
  display:flex;align-items:center;justify-content:center}
.brand-mark span{width:56px;height:56px;border-radius:50%;background:#d89a78}
.brand-name{position:absolute;left:124px;top:7px;width:346px;height:66px;background:var(--dark-panel);
  font-family:"Fresca",sans-serif;font-size:50px;color:var(--cream);line-height:66px;padding-left:16px}
.cart{position:absolute;left:769px;top:7px;width:204px;height:85px;background:var(--brick);
  font-family:"Noto Serif",serif;color:var(--gold);padding:19px 0 0 16px}
.cart .label{font-size:14px}
.cart .total{font-size:15px;font-weight:700;margin-top:4px}
.cart svg{position:absolute;right:18px;top:20px}
.main-nav{position:absolute;left:470px;top:130px;width:503px;height:40px;background:var(--dark-panel);
  display:flex;justify-content:space-evenly;align-items:center;padding:0 24px;
  font-family:"Noto Serif",serif;font-weight:700;font-size:15px;color:var(--gold)}
.content{position:absolute;left:109px;top:196px;width:632px;font-family:"Noto Sans",sans-serif;
  font-size:15px;line-height:27.3px;color:var(--body-text)}
.content h2{font-family:"Noto Serif",serif;font-style:italic;font-weight:700;font-size:28px;color:var(--brick);
  line-height:38px;margin-bottom:2px}
.content p{margin-bottom:27px}
.content h2 + p{margin-top:0}
.sidebar{position:absolute;left:765px;top:206px;width:326px}
.feature{position:relative;height:217px;background:linear-gradient(100deg,#4a3424 0%,#9a7a60 45%,#d8d6cc 100%)}
.connect{position:absolute;left:0;bottom:0;width:100%;height:51px;background:var(--brick-soft);
  display:flex;align-items:center;padding-left:22px;font-family:"Noto Serif",serif;font-weight:700;font-size:19px;color:var(--gold)}
.connect ul{list-style:none;display:flex;gap:16px;margin-left:28px}
.connect li{width:15px;height:15px;background:var(--gold);opacity:.85}
.articles h3{font-family:"Noto Serif",serif;font-weight:700;font-size:20px;color:var(--brick);margin-top:22px;letter-spacing:.3px}
.articles ul{list-style:none;margin-top:8px;font-family:"Noto Serif",serif;font-size:21.5px;color:var(--link-text);line-height:34px}
.shop-banner{margin-top:20px;height:60px;background:linear-gradient(90deg,#8a3a1e,#b0603a,#7a3820);
  font-family:"Noto Serif",serif;font-style:italic;font-weight:700;font-size:28px;color:var(--gold);padding:8px 0 0 24px}
</style>
</head>
<body>
<div class="page">
  <header class="masthead" role="img" aria-label="Close-up photo of handmade organic soap bars">
    <div class="brand-mark"><span></span></div>
    <div class="brand-name">Velm Botanics</div>
    <div class="cart">
      <div class="label">Shopping Cart</div>
      <div class="total">0 items $0.00</div>
      <svg width="54" height="44" viewBox="0 0 54 44" aria-hidden="true">
        <path d="M4 16h46l-6 26H10z" fill="var(--gold)"/>
        <path d="M22 16L36 2" stroke="var(--gold)" stroke-width="5" stroke-linecap="round"/>
        <g stroke="var(--brick)" stroke-width="4"><path d="M18 22v14M27 22v14M36 22v14"/></g>
      </svg>
    </div>
    <nav class="main-nav"><span>Home</span><span>Information</span><span>About Us</span><span>Shop</span></nav>
  </header>

  <main class="content">
    <h2>This is a content header</h2>
    <p>Lorem ipsum dolor sit amet, an dicunt detracto vim, at eum diceret sensibus explicari. Sit at equidem dissentias. Altera civibus adversarium no his, novum tantas cu sed. Nulla probatus id eos, dictas nusquam quo ei. Eum ipsum viris aliquip ut.</p>
    <p>Mucius urbanitas scripserit ne has, dolore ignota nec ei. Summo impedit id est, vix vocibus omittantur at. Prompta quaeque id quo, no noluisse reprehendunt est, eam brute luptatum indoctum ut. Latine voluptua reformidans in mei. Id qui graeco accusam, ubique praesent suscipiantur vis cu.</p>
    <h2>A different article heading</h2>
    <p>In nonumes euripidis mea, ad dicam consul sea. Libris maiorum gloriatur ei est, est cu sumo velit altera. Nam ea mutat reprimique intellegebat, utinam fierent id his, sea ut liber zril deleniti. Falli dolor iisque cu cum. An aliquam accusam commune sea, ut est clita regione consetetur. Solet laudem principes mel ne.</p>
    <p>Mei et omittam blandit mentitum, invenire eleifend salutatus sed ut. Te pri partem</p>
  </main>

  <aside class="sidebar">
    <div class="feature" role="img" aria-label="Photo of stacked organic soap bars">
      <div class="connect">CONNECT
        <ul aria-label="Social links"><li></li><li></li><li></li><li></li><li></li></ul>
      </div>
    </div>
    <section class="articles">
      <h3>LATEST ARTICLES</h3>
      <ul>
        <li>This is a content header</li>
        <li>A different article heading</li>
        <li>Yet another article</li>
        <li>One more article title</li>
      </ul>
    </section>
    <div class="shop-banner">Check out our Shop!</div>
  </aside>
</div>
</body>
</html>
```